Bringing Together Disparate Businesses

Growing largely through acquisitions (~50 over the past 7 years) throughout the course of our company history, our organization rebranded in 2019 to four main business units and a corporate entity. While we have continued to acquire more companies, we are looking to take the next step as an organization to bring everyone together under one set of systems with "Operation Bluefern".
We are seeking a design that shows the coordination of business units as a cohesive unit rather than the individual entities they operate as today as we look to leverage on each others strengths and continue to disrupt our industry and grow together.
The "Operation Bluefern" logo does not necessarily need to be used within this design but we are looking for a graphic to create awareness of the entities across our entire organization. The graphic will have many uses but is anticipated to be distributed as a desktop background, mouse pad design, for marketing materials, etc.

```html
<!DOCTYPE html>
<html lang="en">
<head>
<meta charset="utf-8">
<title>Keystar Group – Operation Bluefern</title>
<link rel="stylesheet" href="https://fonts.googleapis.com/css2?family=Montserrat:wght@400;800&display=swap">
<style>
  :root {
    --page-bg: #000000;
    --deep-navy: #0a0f4a;
    --royal-blue: #1a2a9c;
    --grid-cyan: #2fb6ff;
    --ink: #ffffff;
  }
  * { box-sizing: border-box; margin: 0; padding: 0; }
  html, body {
    width: 1173px; height: 1200px; overflow: hidden;
    background: var(--page-bg);
    font-family: "Montserrat", Arial, sans-serif;
    color: var(--ink);
  }
  .wallpaper {
    position: absolute; left: 0; top: 270px;
    width: 1173px; height: 655px; overflow: hidden;
    background:
      radial-gradient(ellipse 60% 50% at 55% 35%, var(--royal-blue) 0%, transparent 70%),
      linear-gradient(180deg, var(--deep-navy) 0%, #16248a 55%, #0b1660 100%);
  }
  .horizon-floor {
    position: absolute; left: 0; right: 0; bottom: 0; height: 165px;
    background:
      radial-gradient(ellipse 45% 35% at 50% 10%, rgba(47,182,255,0.55), transparent 80%),
      linear-gradient(180deg, #1b4fc4 0%, #12379a 40%, #0a1f6a 100%);
  }
  .brand { position: absolute; text-align: center; line-height: 1; white-space: nowrap; }
  .brand-name { font-weight: 800; letter-spacing: 0.5px; }
  .brand-tag { font-weight: 400; letter-spacing: 0.5px; margin-top: 8px; }

  .brand--group { left: 90px; top: 100px; width: 328px; }
  .brand--group .brand-name { font-size: 54px; }
  .group-rule {
    display: flex; align-items: center; gap: 14px; margin-top: 10px;
    font-size: 20px; font-weight: 400; letter-spacing: 3px;
  }
  .group-rule::before, .group-rule::after {
    content: ""; flex: 1; height: 2px; background: var(--ink);
  }

  .brand--rallo { left: 463px; top: 100px; width: 235px; }
  .brand--rallo .brand-name { font-size: 58px; }
  .brand--rallo .brand-tag { font-size: 17px; }

  .brand--delvane { left: 812px; top: 100px; width: 262px; }
  .brand--delvane .brand-name { font-size: 50px; line-height: 58px; }
  .brand--delvane .brand-tag { font-size: 17px; }

  .brand--clearbrook { left: 78px; top: 340px; width: 276px; text-align: right; }
  .brand--clearbrook .brand-name { font-size: 35px; }
  .brand--clearbrook .brand-tag { font-size: 12px; margin-top: 5px; }

  .brand--meridiem { left: 800px; top: 340px; width: 280px; }
  .brand--meridiem .brand-name {
    font-size: 35px; display: flex; align-items: center; justify-content: center; gap: 10px;
  }
  .brand--meridiem .brand-name::before {
    content: ""; width: 24px; height: 24px; border-radius: 50%; background: var(--ink);
  }
  .brand--meridiem .brand-tag { font-size: 10px; margin-top: 6px; }

  .initiative {
    position: absolute; left: 405px; top: 318px; width: 324px;
    text-align: center; font-weight: 800; font-size: 38px;
    letter-spacing: 5px; line-height: 1.2;
  }
</style>
</head>
<body>
  <main class="wallpaper">
    <div class="horizon-floor" role="img" aria-label="Glowing blue perspective grid floor receding to the horizon"></div>

    <div class="brand brand--group">
      <div class="brand-name">KEYSTAR</div>
      <div class="group-rule">GROUP</div>
    </div>

    <div class="brand brand--rallo">
      <div class="brand-name">RALLO</div>
      <div class="brand-tag">A KEYSTAR COMPANY</div>
    </div>

    <div class="brand brand--delvane">
      <div class="brand-name">DELVANE</div>
      <div class="brand-tag">A KEYSTAR COMPANY</div>
    </div>

    <div class="brand brand--clearbrook">
      <div class="brand-name">CLEARBROOK</div>
      <div class="brand-tag">A KEYSTAR COMPANY</div>
    </div>

    <div class="initiative">OPERATION<br>BLUEFERN</div>

    <div class="brand brand--meridiem">
      <div class="brand-name">MERIDIEM</div>
      <div class="brand-tag">A KEYSTAR COMPANY</div>
    </div>
  </main>
</body>
</html>
```